Jewellery company needs a biweekly flyer

Company profile:
Our company is selling jewelry directly from the factories/designers to the public. We do that cost effectively by selling through all kind of channels and therefore our prices are much lower than when that same jewelry is sold by more conventional channels like jewelry stores.

We are now in the process of developing a B to C site and want to attract potential buyers to this side by means of a (two) weekly flyer. This flyer will be distributed in a package together with all sorts of flyers from all kinds of companies and is distributed door by door being enclosed in the weekly local town newspaper.

Our products:
The jewelry we offer ranges from classic to modern pearl-, Italian silver- and gold jewelry. (Please see the examples I enclosed).

Positioning of the products:
We sell high end quality that you can wear every day or for more special occasions but no catwalk designs. You can find the more classic models that we sell in the better jewellery store but our price will be much lower.

Our customers:
Women from the age of 23 years and older
Brides of all ages

The flyer:
Format: A4– 2 sided – full color

Because it will be a (two) weekly flyer we like it to have a fixed format. This fixed format must help to recognize our flyer between all the other flyers that are distributed at the same time.

The flyer must also have a ±75% fixed layout that we every (two)week can fill with new offerings. A part of this fixed layout must be dedicated to bride jewelry.
So this part of the flyer layout is developed once and is re-used every time. Of course it is no problem if the design is made in such a way that the background need another color for every new issue.

The other ±25% of the flyer space, so in total a half A4, will be newly designed every two weeks around a theme. Like mother’s day, Christmas, winter collection, summer collection, a special bridal edition etc, etc. So every (two) weeks we need a new design that will fit in that 25% space of the flyer.
For the purpose of this contest, please take mother’s day as a theme.

The idea is that the part of the flyer that has a fixed layout will bring the recognition and the part that is redesigned every two weeks will bring the freshness of the new offering/theme and makes sure that people know that it is the new offering.

The flyers must say: These are quality products and now they are made available to you against a much better price than you expect.

Remarks:
. This flyer is for the Dutch market but we understand that, if you use text, they will be English.
. If you use a picture that we have to buy from for instance quillbranepix.com that will be no problem
Updates

I added information in the 'must have section'. It is an attempt to explain our question better. 

Target Market(s)

Brides of all ages
We have the feeling that the buying public that we will reach with this kind of mailing is not so hip, more conservative and looking for that gain.

Industry/Entity Type

Jewelry

Requirements
Must have
• Format: A4– 2 sided – full color

Also already stated in the description but only to sum it up:

The total size of the flyer is A4 double sided.
75% of that A4 double sided space must be a fixed layout also containing a bridal section;
25% of that A4 double sided space will contain a new layout every 2 weeks and is therefore not fixed but designed every 2 weeks around a new theme.

Please contact me if I have to explain it more.

```html
<!DOCTYPE html>
<html lang="en">
<head>
<meta charset="utf-8">
<title>Parels – een Persoonlijk Cadeau</title>
<link rel="stylesheet" href="https://fonts.googleapis.com/css2?family=PT+Sans:ital,wght@0,400;0,700;1,400;1,700&display=swap">
<style>
  :root {
    --pink: #e2368a;
    --pink-soft: #ec6fae;
    --panel: #e07fb0;
    --ink: #3a3a3a;
    --grey-text: #6d6d6d;
    --band: #e4e4e4;
    --cream: #f4ecc8;
    --white: #ffffff;
  }
  * { margin: 0; padding: 0; box-sizing: border-box; }
  html, body { width: 849px; height: 1200px; overflow: hidden; background: var(--white); }
  body { font-family: "PT Sans", Arial, sans-serif; }
  .flyer { position: relative; width: 849px; height: 1200px; overflow: hidden; background: var(--white); }
  .shapes { position: absolute; inset: 0; }

  .headline {
    position: absolute; left: 372px; top: 178px;
    font-style: italic; font-weight: 400; font-size: 150px; line-height: 1; color: var(--pink);
    letter-spacing: -2px;
  }
  .subline {
    position: absolute; left: 390px; top: 350px;
    font-style: italic; font-size: 38px; line-height: 1.1; color: var(--ink);
  }
  .promise {
    position: absolute; right: 22px; top: 437px; width: 340px;
    font-style: italic; font-size: 24px; line-height: 31px; color: var(--pink-soft);
    text-align: right;
  }

  .photo { position: absolute; border-radius: 4px; }
  .item-name {
    position: absolute; font-style: italic; font-size: 15px; color: var(--pink);
    text-transform: uppercase; letter-spacing: .3px;
  }
  .item-desc {
    position: absolute; font-style: italic; font-size: 12px; line-height: 1.35;
    color: var(--grey-text); width: 170px;
  }
  .price {
    position: absolute; width: 98px; height: 34px; background: var(--pink-soft);
    color: var(--white); font-size: 17px; display: flex; align-items: center; justify-content: center;
  }

  .brand {
    position: absolute; right: 24px; top: 690px;
    font-weight: 700; font-size: 24px; line-height: 1; color: var(--white); letter-spacing: 1px;
    display: flex; align-items: center; gap: 8px;
  }
  .brand-dot { width: 12px; height: 12px; border-radius: 50%; background: var(--white); }
  .panel-copy {
    position: absolute; right: 24px; top: 730px; width: 170px;
    font-style: italic; font-size: 11.5px; line-height: 1.4; color: var(--white); text-align: right;
  }

  .badge-title {
    position: absolute; left: 62px; top: 928px; width: 130px; text-align: center;
    font-weight: 700; font-size: 21px; line-height: 1.05; color: var(--ink);
  }
  .badge-pct {
    position: absolute; left: 88px; top: 980px; width: 62px; height: 62px; border-radius: 50%;
    background: var(--pink-soft); color: var(--white); font-size: 21px; font-weight: 700;
    display: flex; align-items: center; justify-content: center;
  }
  .badge-offer {
    position: absolute; left: 160px; top: 970px; width: 200px;
    font-size: 20px; line-height: 1.1; color: var(--ink);
  }
  .gift-note {
    position: absolute; left: 385px; top: 1070px; width: 245px; text-align: center;
    font-style: italic; font-size: 14px; line-height: 1.35; color: var(--grey-text);
  }
  .web {
    position: absolute; left: 300px; top: 1140px; width: 330px; text-align: right;
    font-weight: 700; font-size: 22px; line-height: 1.2; color: var(--ink);
  }
</style>
</head>
<body>
<main class="flyer">
  <svg class="shapes" width="849" height="1200" viewBox="0 0 849 1200" aria-hidden="true">
    <polygon points="0,0 95,0 0,120" fill="#e2368a"/>
    <polygon points="0,0 40,0 0,60" fill="#ec6fae"/>
    <polygon points="0,930 849,560 849,660 0,1030" fill="#e4e4e4"/>
    <polygon points="849,1200 849,1100 560,1200" fill="#e4e4e4"/>
    <polygon points="640,612 849,578 849,890 640,890" fill="#e07fb0"/>
    <g stroke="#ec6fae" stroke-width="1.5" fill="none">
      <line x1="297" y1="72" x2="504" y2="70"/>
      <line x1="141" y1="200" x2="205" y2="190"/>
      <line x1="205" y1="378" x2="311" y2="440"/>
      <line x1="198" y1="595" x2="228" y2="592"/>
      <line x1="250" y1="735" x2="340" y2="705"/>
      <line x1="460" y1="705" x2="478" y2="765"/>
    </g>
    <circle cx="127" cy="990" r="84" fill="#f4ecc8"/>
    <rect x="150" y="958" width="228" height="82" fill="#f4ecc8"/>
    <polygon points="100,1050 125,1110 140,1085 160,1100 150,1050" fill="#e07fb0"/>
  </svg>

  <div class="photo" role="img" aria-label="Dark pearl bracelet" style="left:100px;top:20px;width:197px;height:104px;background:radial-gradient(#6b5a7a,#f2eef3 70%);"></div>
  <div class="photo" role="img" aria-label="Pearl and gold bracelet" style="left:660px;top:128px;width:160px;height:92px;background:radial-gradient(#e7d9a8,#fbf8ee 70%);"></div>
  <div class="photo" role="img" aria-label="Gold drop earrings" style="left:34px;top:150px;width:107px;height:175px;background:linear-gradient(#f5f0e6,#caa36a 60%,#f5f0e6);"></div>
  <div class="photo" role="img" aria-label="White pearl bracelet with red stone" style="left:311px;top:410px;width:175px;height:100px;background:radial-gradient(#c9485a,#f3eeee 70%);"></div>
  <div class="photo" role="img" aria-label="Gold and silver hoop earrings" style="left:30px;top:535px;width:168px;height:185px;background:radial-gradient(#d6d0c2,#faf9f6 70%);"></div>
  <div class="photo" role="img" aria-label="Multi-strand black pearl necklace" style="left:340px;top:540px;width:120px;height:270px;background:linear-gradient(#eeeeee,#2d2d33 50%,#eeeeee);"></div>
  <div class="photo" role="img" aria-label="White pearl necklace on display bust" style="left:650px;top:915px;width:175px;height:250px;background:linear-gradient(#f7f7f7,#c9c6c2);"></div>
  <div class="photo" role="img" aria-label="Bouquet of spring flowers" style="left:0;top:1030px;width:236px;height:170px;border-radius:0;background:radial-gradient(circle at 50% 60%,#e9b6c6,#9fb772 60%,#ffffff 90%);"></div>

  <h1 class="headline">Parels</h1>
  <p class="subline">een Persoonlijk Cadeau</p>
  <p class="promise">These are quality products and<br>now they are made available<br>to you against a much better<br>price than you expect!</p>

  <span class="item-name" style="left:512px;top:58px;">Item Name</span>
  <p class="item-desc" style="left:512px;top:78px;">Lorem ipsum dolor sit amet, consectetur adipiscing elit.</p>
  <div class="price" style="left:505px;top:132px;">$ 00,00</div>

  <span class="item-name" style="left:212px;top:176px;">Item Name</span>
  <p class="item-desc" style="left:212px;top:196px;width:150px;">Lorem ipsum dolor sit amet, consectetur adipiscing elit.</p>
  <div class="price" style="left:198px;top:258px;">$ 00,00</div>

  <span class="item-name" style="left:40px;top:360px;">Item Name</span>
  <p class="item-desc" style="left:40px;top:380px;width:160px;">Lorem ipsum dolor sit amet, consectetur adipiscing elit.</p>
  <div class="price" style="left:40px;top:433px;">$ 00,00</div>

  <span class="item-name" style="left:232px;top:582px;">Item Name</span>
  <p class="item-desc" style="left:232px;top:602px;width:100px;">Lorem ipsum dolor sit amet, consectetur adipiscing elit.</p>
  <div class="price" style="left:232px;top:652px;">$ 00,00</div>

  <span class="item-name" style="left:85px;top:740px;">Item Name</span>
  <p class="item-desc" style="left:85px;top:760px;width:165px;">Lorem ipsum dolor sit amet, consectetur adipiscing elit.</p>
  <div class="price" style="left:79px;top:806px;">$ 00,00</div>

  <span class="item-name" style="left:470px;top:770px;">Item Name</span>
  <p class="item-desc" style="left:470px;top:790px;width:160px;">Lorem ipsum dolor sit amet, consectetur adipiscing elit.</p>
  <div class="price" style="left:459px;top:835px;">$ 00,00</div>

  <div class="brand"><span class="brand-dot"></span>Lumora</div>
  <p class="panel-copy">Handpicked pearls, Italian silver and gold, sent straight from the makers to you. Classic pieces for every day and special moments.</p>

  <p class="badge-title">MOTHER'S DAY SPECIAL</p>
  <div class="badge-pct">20%</div>
  <p class="badge-offer">DISCOUNT<br>on Selected<br>Items</p>

  <p class="gift-note">Please look at our Mother's Day section for the most wonderful gifts at</p>
  <p class="web">www.lumorapearls.eu/kerst</p>
</main>
</body>
</html>
```